Brivet Networks, Inc. Website redesign

Revamp the website, it is old and outdated. www.brivetnetworksinc.com

Target Market(s)

Information Technology Consulting and Staffing

Coding

Coded - Design and coding required

Number of Pages Required

5+ page

Colors

Designer to choose colors to be used in the design.

Requirements
Must have
• Outlined text boxes just like from the Hollis.us site. A clean look

```html
<!DOCTYPE html>
<html lang="en">
<head>
<meta charset="utf-8">
<title>Brivet Networks, Inc.</title>
<link href="https://fonts.googleapis.com/css2?family=Mulish:wght@400;500;600;700&display=swap" rel="stylesheet">
<style>
:root{
  --red:#a51c35;
  --red-dark:#9a1a31;
  --red-light:#b8203b;
  --text:#444;
  --muted:#6b6b6b;
  --line:#d8d8d8;
  --band:#f6f6f6;
  --black:#050505;
  --white:#fff;
}
*{box-sizing:border-box;margin:0;padding:0}
html,body{width:1200px;height:3115px;overflow:hidden}
body{position:relative;background:var(--band);font-family:'Mulish',sans-serif;color:var(--text)}
.abs{position:absolute}
/* header */
.site-header{left:0;top:0;width:1200px;height:93px;background:var(--white)}
.brand{display:flex;align-items:center;gap:10px;font-weight:700;font-size:24px;color:#111;letter-spacing:1px}
.brand-mark{width:22px;height:22px;background:var(--red)}
.site-header .brand{position:absolute;left:77px;top:32px}
.main-nav{position:absolute;right:79px;top:38px;display:flex;gap:26px;font-size:14px;color:#555;text-transform:uppercase}
.main-nav .active{color:var(--red);display:flex;align-items:center;gap:6px}
.main-nav .active::before{content:"";width:10px;height:10px;background:var(--red);border-radius:2px}
/* hero */
.hero{left:0;top:93px;width:1200px;height:584px;background:linear-gradient(90deg,#eef0f2 0%,#e9edf1 45%,#cfd8e2 70%,#8a96a6 100%)}
.hero-city{left:0;top:520px;width:700px;height:157px;background:linear-gradient(180deg,rgba(220,222,226,0) 0%,#b7b9bf 100%)}
.hero-title{left:80px;top:285px;font-size:38px;font-weight:600;color:var(--red);letter-spacing:.5px}
.hero-text{left:79px;top:358px;width:540px;font-size:17px;line-height:29px;color:#333}
/* services */
.services{left:71px;top:595px;width:1059px;height:300px}
.service{position:absolute;top:78px;width:265px;text-align:center;color:var(--white);font-size:17px}
.service svg{display:block;margin:0 auto 20px}
/* intro */
.intro{left:77px;top:963px;width:1046px;height:271px;border:1px solid var(--line)}
.intro-title{left:240px;top:948px;width:720px;background:var(--band);text-align:center;font-size:25px;color:var(--red)}
.intro p{width:900px;margin:0 auto;text-align:center;font-size:13px;line-height:25px;color:var(--muted)}
.intro p:first-child{margin-top:54px;width:860px}
.intro p+p{margin-top:15px}
/* about */
.about-photo{left:0;top:1313px;width:1200px;height:500px;background:linear-gradient(90deg,#7d7e86 0%,#8d8b90 30%,#3f4e62 55%,#23324a 100%)}
.about-card{left:675px;top:1386px;width:448px;height:500px;background:var(--red-dark);color:var(--white);text-align:center;box-shadow:0 22px 18px -16px rgba(0,0,0,.25)}
.about-card h2{margin-top:56px;font-size:32px;font-weight:600}
.about-card p{width:390px;margin:14px auto 0;font-size:13.5px;line-height:25px}
.about-card p+p{margin-top:13px}
.btn{display:inline-block;margin-top:36px;width:177px;height:47px;line-height:47px;background:var(--white);color:var(--red);font-weight:700;font-size:17px}
/* strategy */
.strategy-title{left:0;top:1945px;width:1200px;text-align:center;font-size:32px;font-weight:600;color:var(--red)}
.strategy-text{left:170px;top:2008px;width:860px;text-align:center;font-size:13px;line-height:25px;color:var(--muted)}
.step{position:absolute;top:2146px;width:160px;text-align:center;font-size:18px;color:#444}
.step svg{display:block;margin:0 auto 22px}
/* news */
.news-band{left:0;top:2355px;width:1200px;height:436px;background:var(--band)}
.news-title{left:0;top:2404px;width:1200px;text-align:center;font-size:32px;font-weight:600;color:var(--red)}
.news-card{position:absolute;top:2472px;width:323px;height:239px;border:1px solid var(--line);padding:0 18px}
.news-card h3{margin-top:42px;font-size:20px;font-weight:500;color:#333}
.news-card p{margin-top:12px;font-size:13px;line-height:25px;color:var(--muted)}
.news-meta{margin-top:18px;border-top:1px solid var(--line);padding-top:18px;display:flex;justify-content:space-between;font-size:13px;color:var(--muted)}
.news-meta span{display:flex;align-items:center;gap:10px}
/* footer */
.site-footer{left:0;top:2791px;width:1200px;height:264px;background:var(--black);color:var(--white)}
.site-footer .brand{position:absolute;left:77px;top:70px;color:var(--white)}
.social{position:absolute;top:149px;width:57px;height:57px;border:2px solid var(--white);border-radius:50%;display:flex;align-items:center;justify-content:center;font-size:18px;font-weight:700}
.footer-head{position:absolute;top:60px;font-size:20px;color:#c2213e}
.footer-links{position:absolute;top:98px;font-size:13px;line-height:38px}
.contact-line{position:absolute;left:802px;display:flex;gap:12px;font-size:13px;line-height:25px}
.copyright{left:0;top:3055px;width:1200px;height:60px;background:var(--red);color:var(--white);text-align:center;line-height:60px;font-size:13px}
</style>
</head>
<body>

<header class="abs site-header">
  <div class="brand"><span class="brand-mark"></span>BRIVET NETWORKS</div>
  <nav class="main-nav">
    <span class="active">Home</span><span>About Us</span><span>Services</span><span>Strategy</span><span>IT News</span><span>Contact</span>
  </nav>
</header>

<div class="abs hero" role="img" aria-label="Businessman in a suit holding a tablet by an office window above a city skyline"></div>
<div class="abs hero-city"></div>
<h1 class="abs hero-title">INTEGRITY MISSION RESULTS</h1>
<p class="abs hero-text">Lorem ipsum dolor sit amet, consectetur adipiscing elit, sed do eiusmod tempor incididunt ut labore et dolore magna.</p>

<section class="abs services">
  <svg width="1059" height="300" viewBox="0 0 1059 300" style="position:absolute;left:0;top:0">
    <defs><filter id="sh" x="-5%" y="-5%" width="110%" height="130%"><feGaussianBlur stdDeviation="8"/></filter></defs>
    <ellipse cx="530" cy="280" rx="520" ry="8" fill="rgba(0,0,0,.12)" filter="url(#sh)"/>
    <polygon points="0,0 270,28 270,252 0,271" fill="#9d1b31"/>
    <polygon points="270,28 530,0 530,271 270,252" fill="#a61d35"/>
    <polygon points="530,0 790,16 790,252 530,271" fill="#ae1e38"/>
    <polygon points="790,16 1059,0 1059,271 790,252" fill="#b8203b"/>
  </svg>
  <div class="service" style="left:3px">
    <svg width="64" height="64" viewBox="0 0 64 64" fill="none" stroke="#fff" stroke-width="2"><rect x="3" y="6" width="58" height="40" rx="3"/><path d="M24 56h16M32 46v10"/><circle cx="32" cy="26" r="12"/><path d="M27 26h10M32 21v10"/></svg>
    Hardware / Software Sales
  </div>
  <div class="service" style="left:266px">
    <svg width="64" height="64" viewBox="0 0 64 64" fill="none" stroke="#fff" stroke-width="2"><circle cx="32" cy="32" r="28" stroke-dasharray="8 4"/><circle cx="32" cy="32" r="20"/><circle cx="32" cy="27" r="6"/><path d="M21 44c3-7 19-7 22 0"/></svg>
    Professional Services
  </div>
  <div class="service" style="left:527px">
    <svg width="64" height="64" viewBox="0 0 64 64" fill="none" stroke="#fff" stroke-width="2"><circle cx="32" cy="28" r="9"/><path d="M28 38h8v6h-8zM4 6h10v14H4zM50 6h10v14H50zM4 44h10v14H4zM50 44h10v14H50zM14 13h10M40 13h10M14 51h14M36 51h14M32 4v15"/></svg>
    Technology Assessment
  </div>
  <div class="service" style="left:792px">
    <svg width="64" height="64" viewBox="0 0 64 64" fill="none" stroke="#fff" stroke-width="2"><rect x="16" y="4" width="36" height="30"/><path d="M22 12h24M22 18h24M22 24h16"/><rect x="6" y="26" width="52" height="30"/><circle cx="20" cy="44" r="5"/><circle cx="44" cy="44" r="5"/><path d="M2 58h60"/></svg>
    Technology Consulting
  </div>
</section>

<section class="abs intro">
  <p>Brivet Networks, Inc. is an 8(a) full-service IT consulting company based in the Washington, DC Metro area. We offer specialized, highly customized technology solutions for our customers located throughout the United States. Learn about our Services now.</p>
  <p>No two businesses are the same. We believe the technology supporting your business operations should align with your company. Every project begins with a thorough analysis of your current technology environment. We work with you to define the environment you want. Then we implement industry-proven practices that enable you to achieve your business objectives. We draw on our experience at civilian and federal agencies to generate ideas and create IT solutions that address your unique business needs. Learn about our Strategies.</p>
</section>
<h2 class="abs intro-title">Bringing Thought Leadership and Quality to Every Project</h2>

<div class="abs about-photo" role="img" aria-label="IT consultant with arms crossed standing in a server room"></div>
<section class="abs about-card">
  <h2>ABOUT US</h2>
  <p>Brivet Networks, Inc. is an 8(a) innovative and rapidly growing full-service IT consulting firm. We provide our clients with cutting-edge technologies and the know-how to apply them to their individual business models.</p>
  <p>For over 20 + years, we have been providing reliable IT solutions to businesses in the Washington, DC Metro area and beyond. Our comprehensive services provide clients with unique technology solutions that are customized to meet the specific demands of their business.</p>
  <span class="btn">READ MORE</span>
</section>

<h2 class="abs strategy-title">OUR STRATEGY</h2>
<p class="abs strategy-text">Civilian and Federal agencies are facing increased demands driven by the changing economic environment and shifts in the way products and services are sold and delivered. These factors have created an imperative to leverage new and innovative technology solution architectures like cloud computing to help reduce cost and deliver profit-driving IT capabilities faster than ever before.</p>

<div class="step" style="left:93px">
  <svg width="88" height="96" viewBox="0 0 88 96"><polygon points="44,2 86,26 86,70 44,94 2,70 2,26" fill="#fff" stroke="#ddd" stroke-width="1.5"/><rect x="27" y="31" width="34" height="34" fill="var(--red)"/><path d="M33 58v-8M40 58v-14M47 58v-10M54 58v-17" stroke="#fff" stroke-width="4"/></svg>
  Assess
</div>
<div class="step" style="left:306px">
  <svg width="88" height="96" viewBox="0 0 88 96"><polygon points="44,2 86,26 86,70 44,94 2,70 2,26" fill="#fff" stroke="#ddd" stroke-width="1.5"/><rect x="24" y="46" width="9" height="17" fill="var(--red)"/><path d="M36 63V46l8-14c3 0 5 2 4 6l-2 6h12c3 0 4 3 3 5l-4 12c-1 2-2 2-4 2z" fill="var(--red)"/></svg>
  Recommend
</div>
<div class="step" style="left:521px">
  <svg width="88" height="96" viewBox="0 0 88 96"><polygon points="44,2 86,26 86,70 44,94 2,70 2,26" fill="#fff" stroke="#ddd" stroke-width="1.5"/><polygon points="44,28 63,38 63,58 44,68 25,58 25,38" fill="var(--red)"/><path d="M25 38l19 10 19-10M44 48v20M34 33l19 10M54 33l-19 10M25 48l19 10 19-10" stroke="#fff" stroke-width="2" fill="none"/></svg>
  Implement
</div>
<div class="step" style="left:736px">
  <svg width="88" height="96" viewBox="0 0 88 96"><polygon points="44,2 86,26 86,70 44,94 2,70 2,26" fill="#fff" stroke="#ddd" stroke-width="1.5"/><rect x="23" y="32" width="42" height="27" rx="2" fill="var(--red)"/><path d="M29 51l7-7 5 4 7-9 5 5 6-6" stroke="#fff" stroke-width="2" fill="none"/><path d="M37 65h14M44 59v6" stroke="var(--red)" stroke-width="3"/></svg>
  Monitor
</div>
<div class="step" style="left:950px">
  <svg width="88" height="96" viewBox="0 0 88 96"><polygon points="44,2 86,26 86,70 44,94 2,70 2,26" fill="#fff" stroke="#ddd" stroke-width="1.5"/><circle cx="40" cy="44" r="11" fill="none" stroke="var(--red)" stroke-width="7" stroke-dasharray="5 3"/><circle cx="40" cy="44" r="4" fill="var(--red)"/><path d="M49 53l12 12" stroke="var(--red)" stroke-width="6" stroke-linecap="round"/></svg>
  Manage
</div>

<div class="abs news-band"></div>
<h2 class="abs news-title">IT NEWS</h2>
<article class="news-card" style="left:77px">
  <h3>News Title</h3>
  <p>Lorem Ipsum is simply dummy text of the printing and typesetting industry.</p>
  <div class="news-meta"><span>by admin</span><span><svg width="20" height="16" viewBox="0 0 20 16"><rect x="1" y="2" width="18" height="13" fill="none" stroke="var(--red)" stroke-width="1.5"/><path d="M1 6h18M6 6v9M10 6v9M14 6v9M1 10h18" stroke="var(--red)" stroke-width="1"/></svg>12 APR 2019</span></div>
</article>
<article class="news-card" style="left:439px">
  <h3>News Title</h3>
  <p>Lorem Ipsum is simply dummy text of the printing and typesetting industry.</p>
  <div class="news-meta"><span>by admin</span><span><svg width="20" height="16" viewBox="0 0 20 16"><rect x="1" y="2" width="18" height="13" fill="none" stroke="var(--red)" stroke-width="1.5"/><path d="M1 6h18M6 6v9M10 6v9M14 6v9M1 10h18" stroke="var(--red)" stroke-width="1"/></svg>12 APR 2019</span></div>
</article>
<article class="news-card" style="left:800px">
  <h3>News Title</h3>
  <p>Lorem Ipsum is simply dummy text of the printing and typesetting industry.</p>
  <div class="news-meta"><span>by admin</span><span><svg width="20" height="16" viewBox="0 0 20 16"><rect x="1" y="2" width="18" height="13" fill="none" stroke="var(--red)" stroke-width="1.5"/><path d="M1 6h18M6 6v9M10 6v9M14 6v9M1 10h18" stroke="var(--red)" stroke-width="1"/></svg>12 APR 2019</span></div>
</article>

<footer class="abs site-footer">
  <div class="brand"><span class="brand-mark" style="background:#fff"></span>BRIVET NETWORKS</div>
  <span class="social" style="left:79px">f</span>
  <span class="social" style="left:150px">in</span>
  <div class="footer-head" style="left:440px">SITEMAP</div>
  <div class="footer-links" style="left:440px">Home<br>About us<br>Services</div>
  <div class="footer-links" style="left:618px">Strategy<br>IT News<br>Contact</div>
  <div class="footer-head" style="left:802px">CONTACT INFO</div>
  <div class="contact-line" style="top:96px"><svg width="16" height="22" viewBox="0 0 16 22"><path d="M8 1a7 7 0 0 0-7 7c0 5 7 13 7 13s7-8 7-13a7 7 0 0 0-7-7z" fill="#fff"/><circle cx="8" cy="8" r="3" fill="#000"/></svg><span>2280 Harrowgate Ln Silverbrook,<br>MD 20914</span></div>
  <div class="contact-line" style="top:158px"><svg width="18" height="18" viewBox="0 0 18 18"><path d="M4 1l3 4-2 2c1 3 3 5 6 6l2-2 4 3-2 3C8 17 1 10 1 3z" fill="#fff"/></svg><span>301-555-0147</span></div>
</footer>
<div class="abs copyright">©BRIVET NETWORKS. 2019 - All Rights Reserved.</div>

</body>
</html>
```